Business Card Design Project

I require a business card with the following information on them for various different people;
name
m:
f:
e:
I have a logo already and will attached that. We are in the construction industry. I require something clean and simple but eye catching at the same time. You can use another colour with our logo if you like and you can style the logo as well if you wish. I am open.
Also it needs to be front and back design.
Industry/Entity Type
Construction
Requirements
Must have
- Logo, name, mobile, fax and email address.
Front and back design

```html
<!DOCTYPE html>
<html lang="en">
<head>
<meta charset="utf-8">
<title>Northgate Builders – Business Card</title>
<link href="https://fonts.googleapis.com/css2?family=Didact+Gothic&display=swap" rel="stylesheet">
<style>
  :root {
    --page-bg: #e9e6e1;
    --card-bg: #241d34;
    --card-edge: #1a1526;
    --brand-green: #5cbf45;
    --text-light: #d9d7de;
    --text-muted: #a7a3b2;
  }
  * { box-sizing: border-box; margin: 0; padding: 0; }
  html, body {
    width: 1200px;
    height: 1000px;
    overflow: hidden;
    background: var(--page-bg);
    font-family: "Didact Gothic", "Century Gothic", sans-serif;
  }
  .card-sheet {
    position: relative;
    width: 1200px;
    height: 1000px;
  }
  .card {
    position: absolute;
    top: 190px;
    width: 380px;
    height: 620px;
    background: var(--card-bg);
    box-shadow: 0 0 0 1px var(--card-edge) inset;
  }
  .card--front {
    left: 170px;
    clip-path: polygon(0 90px, 42% 0, 100% 0, 100% 100%, 0 100%);
  }
  .card--back {
    left: 650px;
    clip-path: polygon(0 0, 62% 0, 100% 130px, 100% 100%, 0 100%);
  }
  .brand-mark {
    position: absolute;
    left: 120px;
    top: 60px;
    display: flex;
    align-items: center;
    gap: 10px;
    color: var(--brand-green);
    font-size: 30px;
    letter-spacing: 0.5px;
  }
  .brand-mark__square {
    width: 18px;
    height: 18px;
    background: var(--brand-green);
  }
  .card-details {
    position: absolute;
    left: 50px;
    top: 330px;
  }
  .company-name {
    color: var(--brand-green);
    font-size: 24px;
    line-height: 1.1;
  }
  .person-name {
    margin-top: 30px;
    color: var(--brand-green);
    font-size: 21px;
  }
  .person-role {
    color: var(--text-light);
    font-size: 15px;
    margin-top: 2px;
  }
  .contact-list {
    margin-top: 48px;
    list-style: none;
  }
  .contact-list li {
    display: flex;
    gap: 14px;
    font-size: 15px;
    line-height: 1.35;
    color: var(--text-light);
  }
  .contact-list .contact-label {
    width: 12px;
    color: var(--brand-green);
  }
</style>
</head>
<body>
  <main class="card-sheet">
    <section class="card card--front" aria-label="Card front">
      <div class="brand-mark">
        <span class="brand-mark__square"></span>
        <span class="brand-mark__name">Northgate</span>
      </div>
    </section>

    <section class="card card--back" aria-label="Card back">
      <div class="card-details">
        <p class="company-name">Northgate Builders</p>
        <p class="person-name">Employee Name</p>
        <p class="person-role">Employee Position</p>
        <ul class="contact-list">
          <li><span class="contact-label">m</span><span>(0)19 802 461</span></li>
          <li><span class="contact-label">f</span><span>(0)19 802 462</span></li>
          <li><span class="contact-label">e</span><span>employee1@ngbuild.com</span></li>
        </ul>
      </div>
    </section>
  </main>
</body>
</html>
```